Wordpress and Elementor Pro website

We need a Wordpress/Elementor Pro design for our website. We already have a logo design and installed Wordpress. We have some ideas concerning the design, and we will share two websites. Both the design and content placement we like about these websites. We would like to see designs that use the color Purple (the same as the logo color), white and black. We provide these services: SEO optimization, SEO copywriting and online campaigns. We will provide a list of the page's we would like to see in the design.

Target Market(s)

Entrepreneurs, business owners. Companies who would like to expand online with texts and SEO.

Industry/Entity Type

Digital Marketing

Coding

Coded - Design and coding required

Number of Pages Required

5+ page

Font styles to use
Sans Serif

Colors
886aae
fffefd
0355a3

Requirements
Must have
• Single pages and singel posts of Elementor so I can create new pages and blog posts in the future.

```html
<!DOCTYPE html>
<html lang="nl">
<head>
<meta charset="utf-8">
<title>Veltmark Specialisten</title>
<link href="https://fonts.googleapis.com/css2?family=Poppins:wght@300;400;500;600;700;800&display=swap" rel="stylesheet">
<style>
:root{
  --purple:#6a33a6;
  --purple-soft:#8a6ab8;
  --purple-pale:#efe9f7;
  --blue:#0355a3;
  --blue-deep:#0a4c94;
  --ink:#14112a;
  --grey:#7b7b88;
  --white:#fffefd;
}
*{box-sizing:border-box;margin:0;padding:0}
html,body{width:1200px;height:4380px;overflow:hidden;background:var(--white)}
body{font-family:'Poppins',sans-serif;color:var(--ink);position:relative}
.abs{position:absolute}
.band{position:absolute;left:0;width:1200px}
.band svg{display:block}

/* header */
.brand{left:109px;top:30px;display:flex;align-items:center;gap:8px;color:var(--white);font-weight:600;font-size:15px;letter-spacing:.5px}
.brand-box{width:20px;height:20px;border:2px solid var(--white);border-radius:3px}
.nav{left:585px;top:35px;display:flex;gap:30px;font-size:11px;color:var(--white);letter-spacing:.4px}
.btn{display:flex;align-items:center;justify-content:center;background:var(--blue);color:var(--white);font-size:11px;font-weight:500;letter-spacing:.5px}
.nav-cta{left:925px;top:20px;width:167px;height:46px}

/* hero */
.hero-title{left:109px;top:252px;color:var(--white);font-weight:800;font-size:38px;line-height:52px;letter-spacing:1px;white-space:nowrap}
.hero-text{left:109px;top:375px;color:var(--white);font-size:13px;line-height:26px}
.hero-cta{left:109px;top:452px;width:195px;height:47px}
.hero-art{left:470px;top:185px;width:730px;height:435px;border-radius:6px;background:linear-gradient(135deg,#7d4cb8,#5b2b95)}

/* section heads */
.eyebrow{font-size:11px;letter-spacing:.3px;color:var(--ink)}
.h2{font-weight:700;font-size:32px;color:var(--ink)}
.center{text-align:center}

/* services */
.service{width:300px;text-align:center}
.service .icon{width:106px;height:106px;margin:0 auto;border-radius:50%;background:var(--white);box-shadow:0 4px 14px rgba(60,30,110,.14);display:flex;align-items:center;justify-content:center}
.service h3{margin-top:26px;font-size:19px;font-weight:700;color:var(--blue)}
.service p{margin-top:12px;font-size:13px;line-height:24px;color:var(--grey)}

.quote{left:0;width:1200px;top:1292px;text-align:center;color:var(--white);font-weight:700;font-size:32px;line-height:39px}

.partners{left:115px;top:1640px;width:970px;display:flex;justify-content:space-between}
.partner{width:130px;height:36px;border-radius:4px;background:var(--purple-soft);opacity:.8}

/* about */
.about-title{left:154px;top:1935px;color:var(--white);font-weight:700;font-size:30px}
.about-text{left:154px;top:1984px;width:415px;color:var(--white);font-size:13.5px;line-height:22.5px}
.about-link{left:154px;top:2138px;color:var(--white);font-size:13px;display:flex;gap:10px;align-items:center}
.about-square{left:740px;top:1870px;width:103px;height:103px;background:rgba(255,255,255,.18)}
.about-photo{left:765px;top:1895px;width:270px;height:277px;background:linear-gradient(160deg,#b5b0ac,#6c7a8e)}

/* features */
.feature{width:280px;text-align:center}
.feature h4{margin-top:14px;font-size:16px;font-weight:600}
.feature p{margin-top:12px;font-size:13px;line-height:23px;color:var(--grey)}

/* download */
.pdf-cover{left:170px;top:2732px;width:235px;height:310px;background:linear-gradient(180deg,#6a33a6 0 12%,#f4f1f8 12% 62%,#6a33a6 62%);box-shadow:0 6px 20px rgba(0,0,0,.2)}
.pdf-cover-title{left:170px;top:2736px;width:235px;text-align:center;color:var(--white);font-size:15px;font-weight:600}
.pdf-title{left:437px;top:2767px;color:var(--white);font-weight:500;font-size:24px}
.pdf-text{left:437px;top:2814px;width:460px;color:var(--white);font-size:11.5px;line-height:22px}
.pdf-input{left:437px;top:2882px;width:248px;height:33px;background:var(--white);font-size:11px;color:var(--ink);padding:10px 12px}
.pdf-btn{left:685px;top:2882px;width:87px;height:33px;background:var(--purple);font-size:10px}
.pdf-check{left:437px;top:2924px;color:var(--white);font-size:11.5px;display:flex;align-items:center;gap:8px}
.tick{width:13px;height:13px;background:var(--white);display:flex;align-items:center;justify-content:center}

/* cases */
.view-all{left:997px;top:3160px;width:94px;height:30px;border:1.5px solid var(--ink);border-radius:3px;font-size:11.5px;display:flex;align-items:center;justify-content:center;gap:8px}
.card-art{width:242px;height:300px}
.card-art.one{left:109px;top:3255px;background:linear-gradient(160deg,#f3eff8,#cdbde3)}
.card-art.two{left:622px;top:3255px;background:linear-gradient(160deg,#f2f2f5,#d3c8e4)}
.card-body{width:200px}
.card-meta{font-size:11.5px;color:var(--grey)}
.card-title{margin-top:9px;font-size:21px;font-weight:700;line-height:27px}
.card-text{margin-top:12px;font-size:12.5px;line-height:22px;color:#3b3950}
.card-link{margin-top:6px;font-size:12.5px;display:flex;gap:8px;align-items:center}

/* cta */
.pill{left:532px;top:3700px;width:136px;height:28px;background:var(--purple-pale);color:var(--purple-soft);font-size:11px;display:flex;align-items:center;justify-content:center}
.cta-title{left:0;width:1200px;top:3740px;text-align:center;font-weight:700;font-size:30px;color:var(--ink)}
.cta-btn{left:503px;top:3810px;width:194px;height:46px}
.call{left:0;width:1200px;top:3876px;display:flex;justify-content:center;align-items:center;gap:6px;font-size:11.5px;color:var(--grey)}
.call strong{font-size:19px;font-weight:400;color:var(--ink)}

/* footer */
.foot-brand{left:109px;top:4127px;display:flex;align-items:center;gap:10px;color:var(--white);font-size:22px;font-weight:500;letter-spacing:.5px}
.foot-brand .brand-box{width:30px;height:30px}
.foot-col{color:var(--white)}
.foot-col h5{font-size:14px;font-weight:600;margin-bottom:18px}
.foot-col p{font-size:11.5px;line-height:23px}
.socials{display:flex;gap:16px}
.socials span{width:15px;height:15px;border-radius:50%;background:var(--white)}
.copy{left:0;width:1200px;top:4298px;text-align:center;color:var(--white);font-size:11.5px}
</style>
</head>
<body>

<!-- hero band -->
<div class="band" style="top:0">
  <svg width="1200" height="730"><polygon points="0,0 1200,0 1200,645 0,726" fill="var(--purple)"/></svg>
</div>
<div class="abs brand"><span class="brand-box"></span>VELTMARK</div>
<nav class="abs nav"><span>HOME</span><span>SERVICES</span><span>CASES</span><span>TEAM</span><span>BLOG</span></nav>
<div class="abs btn nav-cta">CONTACT US</div>
<div class="abs hero-art" role="img" aria-label="Illustration of a marketing team working together around an office desk"></div>
<h1 class="abs hero-title">SUCCESSFUL<br>WITH VELTMARK</h1>
<p class="abs hero-text">Lorem ipsum dolor sit amet,<br>consectetur adipisicing elit, sed do.</p>
<div class="abs btn hero-cta">LEARN MORE</div>

<!-- services -->
<p class="abs eyebrow center" style="left:0;width:1200px;top:752px">WHAT WE OFFER?</p>
<h2 class="abs h2 center" style="left:0;width:1200px;top:770px">Our Services</h2>

<div class="abs service" style="left:88px;top:860px">
  <div class="icon"><svg width="48" height="52" viewBox="0 0 48 52" fill="none" stroke="var(--purple)" stroke-width="2"><rect x="6" y="4" width="30" height="42" rx="2"/><line x1="12" y1="16" x2="30" y2="16"/><line x1="12" y1="24" x2="30" y2="24"/><line x1="12" y1="32" x2="26" y2="32"/><line x1="40" y1="10" x2="40" y2="40"/></svg></div>
  <h3>SEO Copywriting</h3>
  <p>Lorem ipsum dolor sit amet,<br>consectetur adipisicing elit, sed do<br>eiusmod tempor incididunt ut labore</p>
</div>
<div class="abs service" style="left:450px;top:860px">
  <div class="icon"><svg width="52" height="52" viewBox="0 0 52 52" fill="none" stroke="var(--purple)" stroke-width="2"><line x1="10" y1="44" x2="10" y2="36"/><line x1="18" y1="44" x2="18" y2="30"/><line x1="26" y1="44" x2="26" y2="26"/><line x1="34" y1="44" x2="34" y2="20"/><line x1="42" y1="44" x2="42" y2="14"/><polyline points="8,28 20,18 28,22 44,6"/><polyline points="36,6 44,6 44,14"/></svg></div>
  <h3>Search Engine Optimization</h3>
  <p>Lorem ipsum dolor sit amet,<br>consectetur adipisicing elit, sed do<br>eiusmod tempor incididunt ut labore</p>
</div>
<div class="abs service" style="left:812px;top:860px">
  <div class="icon"><svg width="52" height="48" viewBox="0 0 52 48" fill="none" stroke="var(--purple)" stroke-width="2"><rect x="4" y="4" width="44" height="34" rx="2"/><line x1="4" y1="12" x2="48" y2="12"/><rect x="14" y="18" width="8" height="12"/><polygon points="22,18 36,14 36,34 22,30"/><line x1="20" y1="44" x2="32" y2="44"/></svg></div>
  <h3>Online Campaigns</h3>
  <p>Lorem ipsum dolor sit amet,<br>consectetur adipisicing elit, sed do<br>eiusmod tempor incididunt ut labore</p>
</div>

<!-- quote band -->
<div class="band" style="top:1160px">
  <svg width="1200" height="355"><defs><linearGradient id="qg" x1="0" x2="1"><stop offset="0" stop-color="#0c4f97"/><stop offset=".5" stop-color="#2160ad"/><stop offset="1" stop-color="#0a4c94"/></linearGradient></defs><polygon points="0,35 1200,0 1200,280 0,355" fill="url(#qg)"/></svg>
</div>
<p class="abs quote">“Omdat online groeien in omzet en<br>winst een specialisme is.”</p>

<!-- partners -->
<div class="abs partners" aria-label="Featured in">
  <span class="partner"></span><span class="partner"></span><span class="partner"></span><span class="partner"></span><span class="partner"></span>
</div>

<!-- about band -->
<div class="band" style="top:1780px">
  <svg width="1200" height="510"><defs><linearGradient id="ag" x1="0" x2="1"><stop offset="0" stop-color="#5e2c9a"/><stop offset=".6" stop-color="#7344ad"/><stop offset="1" stop-color="#6a39a6"/></linearGradient></defs><polygon points="0,75 1200,0 1200,430 0,510" fill="url(#ag)"/></svg>
</div>
<h2 class="abs about-title">About Us</h2>
<p class="abs about-text">Lorem ipsum dolor sit amet, consectetur adipisicing elit, sed do eiusmod tempor incididunt ut labore et dolore magna aliqua. Ut enim ad minim veniam, quis nostrud exercitation ullamco laboris nisi ut aliquip ex ea commodo consequat. Duis aute irure dolor in reprehenderit in voluptate velit esse cillum dolore eu fugiat nulla pariatur.</p>
<div class="abs about-link">Learn more <svg width="14" height="8" viewBox="0 0 14 8" fill="none" stroke="currentColor" stroke-width="1.3"><line x1="0" y1="4" x2="13" y2="4"/><polyline points="9,1 13,4 9,7"/></svg></div>
<div class="abs about-square"></div>
<div class="abs about-photo" role="img" aria-label="Portrait photo of a smiling team member with glasses"></div>

<!-- features -->
<div class="abs feature" style="left:137px;top:2365px">
  <svg width="60" height="60" viewBox="0 0 60 60" fill="none" stroke="var(--purple)" stroke-width="2"><circle cx="24" cy="26" r="14"/><line x1="18" y1="46" x2="30" y2="46"/><line x1="20" y1="52" x2="28" y2="52"/><circle cx="44" cy="14" r="7"/><circle cx="44" cy="14" r="2"/></svg>
  <h4>Strategy</h4>
  <p>Online Veltmark starts<br>with a thorough analysis<br>and clear targets.</p>
</div>
<div class="abs feature" style="left:460px;top:2362px">
  <svg width="62" height="62" viewBox="0 0 62 62" fill="none" stroke="var(--purple)" stroke-width="2"><circle cx="10" cy="10" r="6"/><circle cx="52" cy="10" r="6"/><circle cx="10" cy="52" r="6"/><circle cx="52" cy="52" r="6"/><rect x="22" y="24" width="18" height="14"/><line x1="16" y1="10" x2="46" y2="10"/><line x1="16" y1="52" x2="46" y2="52"/><line x1="14" y1="14" x2="22" y2="24"/><line x1="48" y1="14" x2="40" y2="24"/><line x1="14" y1="48" x2="22" y2="38"/><line x1="48" y1="48" x2="40" y2="38"/></svg>
  <h4>Traffic</h4>
  <p>More relevant visitors to your<br>website thanks to search engine<br>and social media marketing.</p>
</div>
<div class="abs feature" style="left:783px;top:2365px">
  <svg width="62" height="60" viewBox="0 0 62 60" fill="none" stroke="var(--purple)" stroke-width="2"><rect x="6" y="40" width="8" height="16"/><rect x="18" y="32" width="8" height="24"/><rect x="30" y="26" width="8" height="30"/><rect x="42" y="20" width="8" height="36"/><polyline points="4,36 20,24 32,28 48,12"/><circle cx="48" cy="9" r="7"/></svg>
  <h4>Conversion</h4>
  <p>More turnover from your visitors<br>through better content, A / B testing<br>and marketing automation.</p>
</div>

<!-- download band -->
<div class="band" style="top:2632px">
  <svg width="1200" height="425"><defs><linearGradient id="dg" x1="0" x2="1"><stop offset="0" stop-color="#0b4d98"/><stop offset=".5" stop-color="#0355a3"/><stop offset="1" stop-color="#2a63a8"/></linearGradient></defs><polygon points="0,80 1200,0 1200,345 0,425" fill="url(#dg)"/></svg>
</div>
<div class="abs pdf-cover" role="img" aria-label="Cover of the downloadable marketing guide with an illustration of a specialist at a board"></div>
<p class="abs pdf-cover-title">Veltmark Specialisten</p>
<h3 class="abs pdf-title">PDF Download Veltmark Specialisten, fill email!</h3>
<p class="abs pdf-text">Lorem ipsum dolor sit amet, consectetur adipisicing elit, sed do eiusmod tempor incididunt ut labore et dolore magna aliqua.</p>
<div class="abs pdf-input">Your E-Mail</div>
<div class="abs btn pdf-btn">GET IT</div>
<div class="abs pdf-check"><span class="tick"><svg width="9" height="8" viewBox="0 0 9 8" fill="none" stroke="var(--ink)" stroke-width="1.6"><polyline points="1,4 3.5,6.5 8,1"/></svg></span>I would like to receive news and special offers.</div>

<!-- cases & blog -->
<p class="abs eyebrow" style="left:109px;top:3153px">WHAT'S NEW?</p>
<h2 class="abs h2" style="left:109px;top:3170px">Cases &amp; Blog</h2>
<div class="abs view-all">View All <svg width="12" height="9" viewBox="0 0 12 9" fill="none" stroke="currentColor" stroke-width="1.4"><line x1="0" y1="4.5" x2="11" y2="4.5"/><polyline points="7,1 11,4.5 7,8"/></svg></div>

<div class="abs card-art one" role="img" aria-label="Illustration of two colleagues reviewing work at a laptop"></div>
<div class="abs card-body" style="left:380px;top:3316px">
  <p class="card-meta">Case, 4 min read</p>
  <h3 class="card-title">Lorem ipsum<br>dolor sit amet,</h3>
  <p class="card-text">Lorem ipsum dolor sit amet,<br>consectetur adipisicing elit,<br>sed do eiusmod tempor</p>
  <p class="card-link">Read More <svg width="14" height="9" viewBox="0 0 14 9" fill="none" stroke="currentColor" stroke-width="1.4"><line x1="0" y1="4.5" x2="13" y2="4.5"/><polyline points="9,1 13,4.5 9,8"/></svg></p>
</div>
<div class="abs card-art two" role="img" aria-label="Illustration of a team meeting around a presentation chart"></div>
<div class="abs card-body" style="left:884px;top:3316px">
  <p class="card-meta">Blog, 4 min read</p>
  <h3 class="card-title">Lorem ipsum<br>dolor sit amet,</h3>
  <p class="card-text">Lorem ipsum dolor sit amet,<br>consectetur adipisicing elit,<br>sed do eiusmod tempor</p>
  <p class="card-link">Read More <svg width="14" height="9" viewBox="0 0 14 9" fill="none" stroke="currentColor" stroke-width="1.4"><line x1="0" y1="4.5" x2="13" y2="4.5"/><polyline points="9,1 13,4.5 9,8"/></svg></p>
</div>

<!-- call to action -->
<div class="abs pill">Let's work together</div>
<h2 class="abs cta-title">Request an online marketing quote immediately.</h2>
<div class="abs btn cta-btn">CONTACT US</div>
<div class="abs call">Or call us now
  <svg width="18" height="18" viewBox="0 0 24 24" fill="none" stroke="var(--ink)" stroke-width="1.8"><path d="M5 3h4l2 5-3 2a12 12 0 0 0 6 6l2-3 5 2v4a2 2 0 0 1-2 2A18 18 0 0 1 3 5a2 2 0 0 1 2-2z"/></svg>
  <strong>(030) 555-0192</strong>
</div>

<!-- footer -->
<div class="band" style="top:3995px">
  <svg width="1200" height="385"><polygon points="0,85 1200,0 1200,385 0,385" fill="var(--purple)"/></svg>
</div>
<div class="abs foot-brand"><span class="brand-box"></span>VELTMARK</div>
<div class="abs foot-col" style="left:470px;top:4120px">
  <h5>Quick Links</h5>
  <p>Cookie Policy<br>Disclaimer<br>Privacy Policy</p>
</div>
<div class="abs foot-col" style="left:658px;top:4120px">
  <h5>Contact</h5>
  <p>Lindelaan 48, Utrecht,<br>NL, Postcode 3512 AB<br>hallo@veltmark.nl<br>+31 (030) 555-0192</p>
</div>
<div class="abs foot-col" style="left:887px;top:4120px">
  <h5>Follow us</h5>
  <div class="socials"><span></span><span></span><span></span><span></span><span></span></div>
</div>
<p class="abs copy">© 2020 Veltmark Specialisten. All rights reserved.</p>

</body>
</html>
```